Messianic Prophetic Timeline

I would like to create a timeline that will fit on a horizontal 11 x 8 1/2 (8 1/2 x11) sheet of paper.
I have two images that will need to be merged.
There should be 7 time points. 1) 457BCE-26 AD, 2) 26 AD-30AD, 3) 30 AD-66 AD, 4) 66AD- 70AD 5) 70 AD, 6) 70AD-20??, and 7) Future
The #6 and #7 from each graphic should be merged. The 30AD-70AD can be dropped. Time point #7 Future has two different texts both need to be preserved, I would like time point #7 to be larger than the other time points.
There are scripture verses that are associated with each block that should be preserved and be more prominent.
These images are from a powerpoint slide, but I want something that can be printed out.
I run a website www.brightfieldlamp.org. I have some brand colors that if can be incorporated or at least have some color cohesion would be great, but that is not as important as readability.
Background images are nice - The idea is one of conflict between light and darkness, two opposing forces, Christ and anti-Christ. Maybe a king on a white horse battling a large serpent dragon
If you can incorporate this quote near timeblock #1-2 "From the decree to restore Jerusalem until Messiah 483 year"
Second quote anywhere "He will make a covenant with many for 7 years"

```html
<!DOCTYPE html>
<html lang="en">
<head>
<meta charset="utf-8">
<title>Messianic Prophetic Timeline</title>
<link href="https://fonts.googleapis.com/css2?family=Black+Ops+One&family=Montserrat:wght@500;600;700;800&display=swap" rel="stylesheet">
<style>
  :root{
    --navy:#0f2033;
    --blue:#2d5fae;
    --green:#0e9460;
    --gold:#f9a91c;
    --flame:#f05a24;
    --deep:#133c6d;
    --ink:#1f1f1f;
    --white:#ffffff;
  }
  *{box-sizing:border-box;margin:0;padding:0}
  html,body{width:1200px;height:927px;overflow:hidden}
  body{font-family:"Montserrat",sans-serif;background:var(--navy);position:relative}
  .masthead{position:absolute;left:0;top:0;width:1200px;height:81px;background:var(--navy);display:flex;align-items:center;justify-content:center}
  .masthead h1{font-family:"Black Ops One",sans-serif;font-weight:400;color:var(--white);font-size:45px;letter-spacing:5px}
  .backdrop{position:absolute;left:0;top:81px;width:1200px;height:782px;
    background:
      radial-gradient(ellipse at 55% 45%, rgba(150,160,205,.55), transparent 45%),
      linear-gradient(180deg,#c9a8c2 0%,#e3b9ae 30%,#eab890 55%,#d8996b 80%,#b98263 100%)}
  .footer{position:absolute;left:0;top:863px;width:1200px;height:64px;background:var(--navy);display:flex;align-items:center;justify-content:center;color:var(--white);font-weight:700;font-size:26px}
  .axis{position:absolute;left:0;top:0}
  .card{position:absolute;width:258px;border-radius:8px;overflow:hidden;text-align:center;display:flex;flex-direction:column}
  .card .era{height:70px;display:flex;align-items:center;justify-content:center;color:var(--white);font-weight:700;font-size:26px}
  .card .theme{height:70px;background:var(--white);display:flex;align-items:center;justify-content:center;font-weight:800;font-size:26px}
  .card .event{height:37px;display:flex;align-items:center;justify-content:center;color:var(--white);font-weight:600;font-size:23px}
  .card .detail{height:96px;background:var(--white);border-radius:0 0 8px 8px;padding-top:16px;color:var(--ink);font-weight:600;font-size:16.5px;line-height:1.3}
  .card .ref{height:24px;display:flex;align-items:center;justify-content:center;color:var(--white);font-weight:600;font-size:14px;line-height:1.15}
  .top{top:137px}
  .bottom{top:531px}
  .bottom .detail{padding-top:14px}
  .c-blue{background:var(--blue)} .c-blue .theme{color:var(--blue)}
  .c-green{background:var(--green)} .c-green .theme{color:var(--green)}
  .c-gold{background:var(--gold)} .c-gold .theme{color:var(--navy)}
  .c-navy{background:var(--navy)} .c-navy .theme{color:var(--deep)}
  .c-flame{background:var(--flame)} .c-flame .theme{color:var(--flame)}
  .c-deep{background:var(--deep)} .c-deep .theme{color:var(--deep)}
  .c-gold .ref{font-size:13.5px;justify-content:space-around}
  .c-navy .detail{padding-top:14px;font-size:16px;line-height:1.1}
  .c-navy .detail hr{border:0;border-top:1.5px solid var(--deep);width:84%;margin:7px auto 5px}
  .c-navy .ref{height:40px;flex-direction:column}
  .c-blue.bottom .detail{height:102px}
  .c-blue.bottom .ref{height:24px}
  .future-frame{position:absolute;left:886px;top:124px;width:280px;height:328px;border:1.5px dashed var(--navy);border-radius:10px}
  .quote{position:absolute;top:601px;height:107px;background:var(--navy);color:var(--white);font-size:17px;line-height:1.1;text-align:center;display:flex;align-items:center;justify-content:center}
  .quote.left{left:0;width:189px}
  .quote.right{left:1007px;width:193px;padding:0 8px}
</style>
</head>
<body>
  <header class="masthead"><h1>MESSIANIC PROPHETIC TIMELINE</h1></header>

  <div class="backdrop" role="img" aria-label="Painted sunset scene of a rider on a white horse battling a great winged serpent dragon"></div>

  <svg class="axis" width="1200" height="927" viewBox="0 0 1200 927" aria-hidden="true">
    <line x1="0" y1="482" x2="1200" y2="482" stroke="#2b2f36" stroke-width="5"/>
    <polyline points="40,466 56,482 40,498" fill="none" stroke="#2b2f36" stroke-width="6"/>
    <g stroke="#2b2f36" stroke-width="1.5">
      <line x1="164" y1="434" x2="164" y2="482"/>
      <line x1="442" y1="434" x2="442" y2="482"/>
      <line x1="732" y1="434" x2="732" y2="482"/>
      <line x1="1024" y1="452" x2="1024" y2="482"/>
      <line x1="318" y1="482" x2="318" y2="531"/>
      <line x1="596" y1="482" x2="596" y2="531"/>
      <line x1="878" y1="482" x2="878" y2="531"/>
    </g>
    <g fill="#fff" stroke-width="4">
      <circle cx="164" cy="482" r="10" stroke="#2d5fae"/>
      <circle cx="318" cy="482" r="10" stroke="#f05a24"/>
      <circle cx="442" cy="482" r="10" stroke="#0e9460"/>
      <circle cx="596" cy="482" r="10" stroke="#133c6d"/>
      <circle cx="732" cy="479" r="10" stroke="#f9a91c"/>
      <circle cx="878" cy="482" r="10" stroke="#2d5fae"/>
      <circle cx="1024" cy="482" r="10" stroke="#0f2033"/>
    </g>
  </svg>

  <div class="future-frame"></div>

  <section class="card top c-blue" style="left:35px">
    <div class="era">457 BCE - 26 AD</div>
    <div class="theme">MESSIAH</div>
    <div class="event">Cut Off</div>
    <div class="detail">483 years from<br>decree</div>
    <div class="ref">Dan 9:26, Ezra 7,9:9</div>
  </section>

  <section class="card top c-green" style="left:314px">
    <div class="era">30 AD-66 AD</div>
    <div class="theme">APOSTLES</div>
    <div class="event">Persecution</div>
    <div class="detail">In Synagogue By family,<br>friends By Kings</div>
    <div class="ref">Luke 21:12-19</div>
  </section>

  <section class="card top c-gold" style="left:600px">
    <div class="era">70 AD++</div>
    <div class="theme">JERUSALEM</div>
    <div class="event">Desolation</div>
    <div class="detail">Dispersed in<br>nations</div>
    <div class="ref"><span>Lk 21:24 Is 61:2 Hos 9:7</span><span>|</span><span>Dan 9:26</span></div>
  </section>

  <section class="card top c-navy" style="left:897px">
    <div class="era">Future</div>
    <div class="theme">COVENANT</div>
    <div class="event">Made</div>
    <div class="detail">Stops Sacrifice Causes<hr>Abomination of<br>Desolation</div>
    <div class="ref">Luke 21:25+ Matt 24:15<br>Dan 9:27,11:31,12:11</div>
  </section>

  <section class="card bottom c-flame" style="left:189px">
    <div class="era">26 AD-30AD</div>
    <div class="theme">COVENANT</div>
    <div class="event">Made</div>
    <div class="detail">Jesus Make<br>Covenant with Many,<br>stops Sacrifice</div>
    <div class="ref">Dan 9:27</div>
  </section>

  <section class="card bottom c-deep" style="left:469px">
    <div class="era">66AD- 70AD</div>
    <div class="theme">VENGEANCE</div>
    <div class="event">Days of</div>
    <div class="detail">Jerusalem<br>Surrounded<br>Flee</div>
    <div class="ref">Luke 21:20-23</div>
  </section>

  <section class="card bottom c-blue" style="left:750px">
    <div class="era">70AD-20</div>
    <div class="theme">GENTILES</div>
    <div class="event">Time of</div>
    <div class="detail">Trample<br>Jerusalem</div>
    <div class="ref">Lk 21:8-11,24 Mat 24:4-14</div>
  </section>

  <blockquote class="quote left">“From the decree to<br>restore Jerusalem<br>until Messiah<br>483 year”</blockquote>
  <blockquote class="quote right">“He will make a<br>covenant with<br>many for 7 years”</blockquote>

  <footer class="footer">www.brightfieldlamp.org</footer>
</body>
</html>
```